Law Firm Profile

I need a Law firm Profile design. Something professional, corporate inspired, unique and sophisticated. Preferred colours are blue, grey and white. Completion timeline is 5 days. Details of law firm are in the uploaded document

```html
<!DOCTYPE html>
<html lang="en">
<head>
<meta charset="utf-8">
<title>Halden Rowe Advocates – Law Firm Profile</title>
<link rel="stylesheet" href="https://fonts.googleapis.com/css2?family=Montserrat:wght@500;700;800;900&family=Open+Sans:wght@400;600;700&display=swap">
<style>
:root{
  --navy:#1d2c4c;
  --navy-deep:#14213b;
  --orange:#f39200;
  --ink:#3b4254;
  --muted:#6c7282;
  --stage:#e6e7ea;
  --page:#ffffff;
  --photo-a:#8a94a6;
  --photo-b:#c9ccd3;
}
*{box-sizing:border-box;margin:0;padding:0}
html,body{width:1200px;height:2372px;overflow:hidden;background:var(--stage)}
body{position:relative;font-family:"Open Sans",Arial,sans-serif;color:var(--ink)}
.spread{position:absolute;left:40px;width:1120px;display:flex;background:var(--page);box-shadow:0 6px 24px rgba(0,0,0,.18)}
.page{position:relative;width:560px;height:100%;overflow:hidden}
.page + .page{border-left:1px solid #e3e4e8}
.photo{position:absolute;background:linear-gradient(135deg,var(--photo-a),var(--photo-b))}
.photo.warm{background:linear-gradient(135deg,#7b6a58,#cdbfae)}
.photo.office{background:linear-gradient(135deg,#5b6170,#d3d5da)}
h1,h2,h3{font-family:"Montserrat",Arial,sans-serif}
.body-copy{font-size:10.5px;line-height:1.55;color:var(--ink)}
.body-copy p{margin-bottom:8px}
.body-copy b{color:var(--navy)}
.orange{color:var(--orange)}

/* spread one */
.s1{top:20px;height:780px}
.cover-heading{position:absolute;left:40px;top:40px;font-size:40px;line-height:1.05;font-weight:900;color:var(--navy);text-transform:uppercase}
.cover-heading span{color:var(--orange)}
.contact-panel{position:absolute;left:30px;top:260px;width:500px;height:330px;background:var(--navy);border-radius:0 40px 0 40px;padding:40px 36px;color:#fff}
.contact-panel h2{font-size:30px;font-weight:800;margin-bottom:22px}
.contact-line{display:flex;align-items:center;gap:10px;font-size:12px;margin-bottom:14px;max-width:250px}
.contact-line svg{flex:none}
.team-photo-left{left:300px;top:210px;width:240px;height:200px;border-radius:30px 0 30px 0;border:5px solid #fff}
.accent-bar{position:absolute;background:var(--orange);border-radius:4px}
.cover-title{position:absolute;left:-40px;top:340px;width:560px;height:200px;background:var(--navy);transform:skewY(-6deg);padding:40px 0 0 160px}
.cover-title h1{transform:skewY(6deg);color:#fff;font-size:34px;line-height:1.08;font-weight:900;text-transform:uppercase}
.cover-title h1 span{color:var(--orange);font-size:22px;display:block;margin-bottom:4px}
.web-pill{position:absolute;right:40px;bottom:40px;border:1px solid var(--navy);border-radius:20px;padding:6px 18px;font-size:11px;color:var(--navy);font-weight:600}

/* spread two */
.s2{top:830px;height:700px}
.section-title{font-size:22px;font-weight:800;color:var(--navy)}
.title-band{background:var(--navy);color:#fff;padding:10px 30px;font-size:22px;font-weight:800;text-transform:uppercase;line-height:1.1}
.title-band small{display:block;color:var(--orange);font-size:14px;text-transform:none}

/* spread three */
.s3{top:1560px;height:790px}
.roles{list-style:none;counter-reset:r;padding:40px 50px}
.roles li{counter-increment:r;font-family:"Montserrat",Arial,sans-serif;font-weight:800;color:var(--navy);font-size:17px;margin-bottom:12px;text-transform:uppercase}
.roles li::before{content:counter(r) ". "}
.values-band{margin:10px 50px 0;background:var(--navy);color:var(--orange);font-family:"Montserrat",Arial,sans-serif;font-weight:800;font-size:18px;padding:8px 18px;text-align:right;border-radius:0 18px 0 18px}
</style>
</head>
<body>

<!-- Spread one: contact and cover -->
<section class="spread s1">
  <div class="page">
    <h2 class="cover-heading">Business<br>Address and<br><span>Contact</span><br>Information</h2>
    <div class="accent-bar" style="left:40px;top:222px;width:90px;height:8px"></div>
    <div class="contact-panel">
      <h2>Contact Us</h2>
      <div class="contact-line"><svg width="16" height="16" viewBox="0 0 24 24"><path fill="#f39200" d="M12 2a7 7 0 0 0-7 7c0 5 7 13 7 13s7-8 7-13a7 7 0 0 0-7-7zm0 9.5A2.5 2.5 0 1 1 12 6.5a2.5 2.5 0 0 1 0 5z"/></svg>Plot 14, Acacia Avenue, Fairview Park, Lusaka</div>
      <div class="contact-line"><svg width="16" height="16" viewBox="0 0 24 24"><path fill="#f39200" d="M6.6 10.8a15 15 0 0 0 6.6 6.6l2.2-2.2a1 1 0 0 1 1-.25 11.4 11.4 0 0 0 3.6.57 1 1 0 0 1 1 1V20a1 1 0 0 1-1 1A17 17 0 0 1 3 4a1 1 0 0 1 1-1h3.5a1 1 0 0 1 1 1 11.4 11.4 0 0 0 .57 3.6 1 1 0 0 1-.25 1z"/></svg>+260 211 555 014 / +260 977 555 208</div>
      <div class="contact-line"><svg width="16" height="16" viewBox="0 0 24 24"><path fill="#f39200" d="M2 5h20v14H2zm2 2v.5l8 5 8-5V7z"/></svg>info@haldenrowe-law.example</div>
    </div>
    <div class="photo team-photo-left" role="img" aria-label="Photo of the firm's lawyers in business attire"></div>
    <div class="photo" style="left:0;bottom:0;width:560px;height:150px;opacity:.35" role="img" aria-label="Faded photo of a city office building"></div>
  </div>
  <div class="page">
    <div class="photo" style="left:0;top:0;width:560px;height:360px" role="img" aria-label="Photo of the legal team standing together in an office"></div>
    <div class="cover-title"><h1><span>Halden Rowe</span>Advocates<br>Law Firm<br>Profile</h1></div>
    <div class="accent-bar" style="left:80px;top:300px;width:200px;height:14px;transform:rotate(-6deg)"></div>
    <div class="accent-bar" style="left:300px;top:560px;width:240px;height:14px;transform:rotate(-6deg)"></div>
    <div class="web-pill">www.haldenrowe-law.example</div>
  </div>
</section>

<!-- Spread two: profile and managing partner -->
<section class="spread s2">
  <div class="page" style="padding:34px 40px">
    <h2 class="section-title" style="margin-bottom:14px">Halden Rowe Advocates Law Firm Profile</h2>
    <div class="body-copy">
      <p>Halden Rowe Advocates is a full service law firm registered to practise in all courts of the republic. The firm offers sound legal counsel to individuals, businesses and public bodies, and prides itself on clear advice, prompt service and fair fees.</p>
      <p><b>Litigation:</b> We represent clients in civil and commercial disputes before the High Court, the Court of Appeal and the Supreme Court, as well as in tribunals and arbitration. Our team prepares every case with care and argues it with skill.</p>
      <p><b>Corporate Law:</b> We advise on company formation, governance, mergers, acquisitions and regulatory compliance. We draft and review contracts and guide boards through changes in law that affect their business.</p>
      <p><b>Estate and Family Law:</b> We help clients with wills, probate, estate administration, divorce, custody and maintenance, handling each sensitive matter with discretion and respect.</p>
      <p><b>Debt Collection:</b> We recover debts for lenders, traders and service providers through demand letters, negotiation and court action where needed.</p>
      <p><b>Civil and Criminal Litigation:</b> We defend and prosecute matters in magistrate and subordinate courts and appear for clients in bail, trial and appeal hearings across the country.</p>
      <p><b>Conveyancing:</b> We manage sale and purchase of land, title searches, leases, mortgages and registration of property, making each transfer smooth and secure for buyers and sellers.</p>
      <p><b>Labour Law:</b> We advise employers and employees on contracts, disputes, dismissals and workplace policy, and represent them before the labour courts.</p>
    </div>
  </div>
  <div class="page">
    <div class="title-band" style="margin-top:30px">Key Personnel Managing<br>Partner <small>– Naomi Kalenga</small></div>
    <div class="body-copy" style="padding:18px 40px 0">
      <p>Naomi Kalenga has more than fifteen years of experience in legal practice. She holds a Bachelor of Laws and a Master of Laws in commercial law and was admitted to the bar after completing her studies at the national law school.</p>
      <p>She has led major commercial and constitutional matters, advised banks and public bodies, and served on several legal reform committees. Her practice focuses on corporate advisory, dispute resolution and property law.</p>
      <p>Naomi is a member of the Law Association and serves as a mentor to young advocates. She believes in honest counsel, careful preparation and lasting client relationships.</p>
    </div>
    <div class="photo office" style="left:40px;bottom:40px;width:480px;height:230px;border-radius:0 30px 0 30px" role="img" aria-label="Photo of lawyers meeting at a conference table"></div>
  </div>
</section>

<!-- Spread three: associate, structure and values -->
<section class="spread s3">
  <div class="page" style="padding:34px 40px">
    <h2 class="section-title" style="font-size:26px;text-transform:uppercase">Associate <span class="orange" style="font-size:16px;text-transform:none">– Daniel Banda</span></h2>
    <div class="body-copy" style="margin-top:12px">
      <p>Daniel Banda has over eight years of experience in civil litigation, conveyancing and employment law. He holds a Bachelor of Laws and was admitted as an advocate after completing the legal practitioners course. He has appeared in numerous trials and has advised traders, farmers and private clients on land and contract matters.</p>
    </div>
    <h2 class="orange" style="font-size:28px;font-weight:800;line-height:1.05;margin-top:26px;width:240px">Management Structure</h2>
    <div class="body-copy" style="margin-top:12px;width:250px">
      <p>The firm is led by the managing partner with the support of partners and associates. Each team member has a clear role so that every matter is handled by the right person and clients always know whom to contact.</p>
    </div>
    <div class="photo warm" style="left:310px;top:250px;width:220px;height:300px;border-radius:30px 0 30px 0" role="img" aria-label="Photo of a judge's gavel and law books"></div>
    <div class="photo" style="left:0;bottom:0;width:560px;height:130px;opacity:.3" role="img" aria-label="Faded photo of a courthouse facade"></div>
  </div>
  <div class="page">
    <ol class="roles">
      <li>Managing Partner</li>
      <li>Partner (s)</li>
      <li>Associate (s) Support Staff:</li>
      <li>Office Manager</li>
      <li>Assistant Office Manager</li>
      <li>Legal Clerk</li>
      <li>Receptionist</li>
    </ol>
    <div class="values-band">Core Values</div>
    <div class="body-copy" style="padding:14px 50px 0">
      <p>We act with integrity, respect and diligence. We keep client matters confidential, give honest advice and work as one team to deliver results that protect our clients' interests.</p>
    </div>
    <div class="photo" style="left:0;bottom:0;width:560px;height:250px" role="img" aria-label="Photo of the legal team in a group discussion"></div>
  </div>
</section>

</body>
</html>
```